Business Card Design Project

We consult with hotels on setting rates and maximizing a revenue strategy

Industry/Entity Type

Business

Contact Information for Business Card

I am not sure what I want. Our company offers high level consulting to hotels around the country but we are also laid back. I would like something that is professional but also shows the laid back side

```html
<!DOCTYPE html>
<html lang="en">
<head>
<meta charset="utf-8">
<title>Harborline Business Card</title>
<link href="https://fonts.googleapis.com/css2?family=Lato:wght@400;700&display=swap" rel="stylesheet">
<style>
  :root {
    --teal: #6a9e99;
    --teal-dark: #4f8984;
    --brown: #2e211c;
    --white: #ffffff;
    --ink: #1d1d1d;
    --backdrop: #e4e6e7;
  }
  * { box-sizing: border-box; margin: 0; padding: 0; }
  html, body { width: 1200px; height: 898px; overflow: hidden; }
  body {
    background: var(--backdrop);
    font-family: "Lato", sans-serif;
    position: relative;
  }
  .card {
    position: absolute;
    left: 290px;
    width: 620px;
    height: 354px;
    overflow: hidden;
    box-shadow: 0 6px 18px rgba(0,0,0,0.18);
  }
  .card--front { top: 50px; background: var(--teal); }
  .card--back { top: 470px; background: var(--white); }
  .card svg.swoosh { position: absolute; inset: 0; }

  .front-web {
    position: absolute; right: 40px; top: 34px;
    color: var(--white); font-size: 19px; letter-spacing: 1.5px;
  }
  .brand {
    position: absolute;
    color: var(--brown);
    font-weight: 700;
    display: flex; align-items: center; gap: 12px;
  }
  .brand__mark { background: var(--brown); flex: none; }
  .brand__name { line-height: 1; }
  .brand__tag { display: block; line-height: 1.2; }

  .card--front .brand { right: 40px; bottom: 92px; }
  .card--front .brand__mark { width: 18px; height: 18px; }
  .card--front .brand__name { font-size: 54px; letter-spacing: 1px; text-transform: uppercase; }
  .card--front .brand__tag { font-size: 20px; margin-top: 6px; }

  .card--back .brand { left: 42px; top: 66px; }
  .card--back .brand__mark { width: 12px; height: 12px; }
  .card--back .brand__name { font-size: 30px; text-transform: uppercase; }
  .card--back .brand__tag { font-size: 12px; margin-top: 4px; }

  .person { position: absolute; right: 60px; top: 108px; text-align: right; }
  .person__name { font-size: 26px; color: var(--ink); }
  .person__role { font-size: 17px; color: var(--teal-dark); margin-top: 4px; }

  .contact { position: absolute; left: 46px; top: 204px; list-style: none; }
  .contact li {
    display: flex; align-items: center; gap: 12px;
    font-size: 18px; color: var(--ink); line-height: 26px;
  }
  .contact svg { width: 16px; height: 16px; fill: var(--teal-dark); flex: none; }

  .back-web {
    position: absolute; right: 44px; bottom: 22px;
    color: var(--white); font-size: 18px; letter-spacing: 1.2px;
  }
</style>
</head>
<body>

<section class="card card--front">
  <svg class="swoosh" viewBox="0 0 620 354" width="620" height="354" aria-hidden="true">
    <path d="M0 354 L0 334 C110 300 220 286 330 286 C250 292 130 318 70 354 Z" fill="var(--brown)"/>
  </svg>
  <p class="front-web">www.HarborlineRMS.com</p>
  <div class="brand">
    <span class="brand__mark"></span>
    <div>
      <span class="brand__name">Harborline</span>
      <span class="brand__tag">Revenue Management Solutions</span>
    </div>
  </div>
</section>

<section class="card card--back">
  <svg class="swoosh" viewBox="0 0 620 354" width="620" height="354" aria-hidden="true">
    <path d="M0 336 C300 322 500 262 620 168 L620 354 L0 354 Z" fill="var(--teal)"/>
    <path d="M0 328 C300 314 500 250 620 150 L620 170 C500 264 300 324 0 333 Z" fill="var(--brown)"/>
  </svg>

  <div class="brand">
    <span class="brand__mark"></span>
    <div>
      <span class="brand__name">Harborline</span>
      <span class="brand__tag">Revenue Management Solutions</span>
    </div>
  </div>

  <div class="person">
    <p class="person__name">Dana Whitfield</p>
    <p class="person__role">Regional Revenue Manager</p>
  </div>

  <ul class="contact">
    <li>
      <svg viewBox="0 0 16 16" aria-label="Phone"><path d="M3 1 L6 1 L7 5 L5 6.5 C6 9 7.5 10.5 9.5 11 L11 9 L15 10 L15 13 C15 14 14 15 13 15 C6.5 14.5 1.5 9.5 1 3 C1 2 2 1 3 1 Z"/></svg>
      503-555-0142
    </li>
    <li>
      <svg viewBox="0 0 16 16" aria-label="Fax"><rect x="4" y="1" width="8" height="4"/><rect x="1" y="6" width="14" height="6" rx="1"/><rect x="4" y="10" width="8" height="5" fill="#fff" stroke="var(--teal-dark)" stroke-width="1.5"/></svg>
      503-555-0187
    </li>
    <li>
      <svg viewBox="0 0 16 16" aria-label="Email"><rect x="1" y="3" width="14" height="10"/><path d="M1.5 3.5 L8 9 L14.5 3.5" fill="none" stroke="#fff" stroke-width="1.3"/></svg>
      Dana@HarborlineRMS.com
    </li>
  </ul>

  <p class="back-web">www.HarborlineRMS.com</p>
</section>

</body>
</html>
```